Harlow Crest Holdings (Remodeling company) needs a logo and business card

We need a business card design for a new company. We "flip" upmarket houses (buy, remodel and sell) in the Austin, TX area. I'd like neutral colors (grey, white, gold black). I would like it to include a simple, clean logo. Our designs are modern and uncluttered and I would like that reflected in the business card design.

Target Market(s)

Young professionals, Families, Retirees. Our properties will sell for $750k+

Industry/Entity Type

Real Estate

Contact Information for Business Card

Harlow Crets Holdings
Mona Harlow
(979) 555 0142
Owner
Rolf Tandem
(512) 555 0176
Realtor

Logo Text

Harlow Crest Holdings

Font styles to use
Serif
Script

Requirements
Must have
• Simple, classic design
Nice to have
• Clean lines, modern look
Should not have
• Too traditionally

```html
<!DOCTYPE html>
<html lang="en">
<head>
<meta charset="utf-8">
<title>Harlow Crest Holdings — Business Cards</title>
<link rel="stylesheet" href="https://fonts.googleapis.com/css2?family=Fira+Sans:wght@500;600&display=swap">
<style>
  :root {
    --page-bg: #e9e6ea;
    --card-bg: #1f1f1f;
    --card-bg-light: #2e2e2e;
    --gold: #f3b51a;
    --gold-faint: rgba(200, 160, 40, 0.13);
    --ink: #ffffff;
  }
  * { box-sizing: border-box; margin: 0; padding: 0; }
  html, body { width: 1200px; height: 1040px; overflow: hidden; }
  body {
    background: var(--page-bg);
    font-family: "Fira Sans", sans-serif;
    display: flex;
    align-items: center;
    justify-content: center;
    gap: 80px;
  }
  .card {
    position: relative;
    width: 340px;
    height: 595px;
    background: linear-gradient(160deg, var(--card-bg-light) 0%, var(--card-bg) 60%);
    overflow: hidden;
    box-shadow: 0 12px 30px rgba(0,0,0,0.18);
  }
  .card__decor {
    position: absolute;
    left: 70px; top: 10px;
    width: 230px; height: 320px;
    background: radial-gradient(ellipse at center, var(--gold-faint) 0%, transparent 72%);
  }
  .card__company {
    position: relative;
    margin: 36px 24px 0 0;
    text-align: right;
    color: var(--gold);
    font-weight: 600;
    font-size: 42px;
    line-height: 1.15;
  }
  .card__contact {
    position: relative;
    margin: 36px 24px 0 28px;
    color: var(--ink);
  }
  .contact-row {
    display: flex;
    align-items: flex-start;
    justify-content: space-between;
  }
  .contact-row svg { flex: none; fill: var(--ink); }
  .contact-row__name { font-size: 30px; font-weight: 600; text-align: right; }
  .contact-row__role { font-size: 24px; font-weight: 500; text-align: right; margin-top: 4px; }
  .contact-row--phone { align-items: center; margin-top: 6px; }
  .contact-row__phone { font-size: 27px; font-weight: 600; }
  .card__mark {
    position: absolute;
    left: 28px; right: 24px; bottom: 36px;
    height: 200px;
    display: flex;
    flex-direction: column;
    align-items: flex-start;
    justify-content: flex-end;
    gap: 16px;
    border-left: 3px solid var(--gold);
    border-bottom: 3px solid var(--gold);
    padding: 0 0 18px 20px;
  }
  .card__mark-square {
    width: 44px; height: 44px;
    border: 3px solid var(--gold);
  }
  .card__mark-name {
    color: var(--gold);
    font-size: 26px;
    font-weight: 600;
    line-height: 1.15;
  }
</style>
</head>
<body>

  <article class="card card--realtor">
    <div class="card__decor" role="img" aria-label="Faint large company mark as background decoration"></div>
    <h1 class="card__company">Harlow Crets<br>Holdings</h1>
    <div class="card__contact">
      <div class="contact-row">
        <svg width="30" height="30" viewBox="0 0 24 24" aria-hidden="true"><circle cx="12" cy="7" r="5"/><path d="M2 23c0-6 4-9 10-9s10 3 10 9z"/></svg>
        <div>
          <p class="contact-row__name">Rolf Tandem</p>
          <p class="contact-row__role">Realtor</p>
        </div>
      </div>
      <div class="contact-row contact-row--phone">
        <svg width="24" height="34" viewBox="0 0 16 24" aria-hidden="true"><rect x="2" y="2" width="12" height="20" rx="2" fill="none" stroke="#fff" stroke-width="1.6"/><circle cx="8" cy="19" r="1"/></svg>
        <p class="contact-row__phone">(512) 555 0176</p>
      </div>
    </div>
    <div class="card__mark">
      <span class="card__mark-square" aria-hidden="true"></span>
      <p class="card__mark-name">Harlow Crest<br>Holdings</p>
    </div>
  </article>

  <article class="card card--owner">
    <h1 class="card__company">Harlow Crets<br>Holdings</h1>
    <div class="card__contact">
      <div class="contact-row">
        <svg width="30" height="30" viewBox="0 0 24 24" aria-hidden="true"><circle cx="12" cy="7" r="5"/><path d="M2 23c0-6 4-9 10-9s10 3 10 9z"/></svg>
        <div>
          <p class="contact-row__name">Mona Harlow</p>
          <p class="contact-row__role">Owner</p>
        </div>
      </div>
      <div class="contact-row contact-row--phone">
        <svg width="24" height="34" viewBox="0 0 16 24" aria-hidden="true"><rect x="2" y="2" width="12" height="20" rx="2" fill="none" stroke="#fff" stroke-width="1.6"/><circle cx="8" cy="19" r="1"/></svg>
        <p class="contact-row__phone">(979) 555 0142</p>
      </div>
    </div>
    <div class="card__mark">
      <span class="card__mark-square" aria-hidden="true"></span>
      <p class="card__mark-name">Harlow Crest<br>Holdings</p>
    </div>
  </article>

</body>
</html>
```